Cardiology practice business card

We need a business card for our cardiology practice "Bellmoor Cardiology". We have a new logo, attached below. We like the colours in the logo - red and charcoal. The front of the business card will need to have the doctors name, address, phone number and email. The back will need to have space to write 2 appointment dates and times.

```html
<!DOCTYPE html>
<html lang="en">
<head>
<meta charset="utf-8">
<title>Bellmoor Cardiology – Business Card</title>
<link href="https://fonts.googleapis.com/css2?family=Montserrat:wght@600;700&family=Roboto:wght@400;500&display=swap" rel="stylesheet">
<style>
  :root {
    --red: #e3151a;
    --charcoal: #2b2b2c;
    --charcoal-deep: #232324;
    --white: #ffffff;
    --ink: #3a3a3a;
    --silver: #d9d9d9;
    --dash: #9a9a9a;
    --stage: #e9e9ea;
  }
  * { box-sizing: border-box; margin: 0; padding: 0; }
  html, body { width: 1200px; height: 840px; overflow: hidden; }
  body {
    background: var(--stage);
    font-family: "Roboto", Arial, sans-serif;
    position: relative;
  }
  .card {
    position: absolute;
    width: 640px;
    height: 366px;
    border-radius: 28px;
    border: 3px solid var(--red);
    overflow: hidden;
  }

  /* ---------- Appointment side ---------- */
  .card--appointment { left: 60px; top: 40px; background: var(--white); }
  .appointment__head {
    position: absolute; left: 0; top: 0; width: 100%; height: 140px;
    background: var(--charcoal);
    border-bottom: 5px solid var(--red);
  }
  .brand-name {
    position: absolute;
    font-family: "Montserrat", Arial, sans-serif;
    font-weight: 700;
    color: var(--red);
    letter-spacing: 0.5px;
    white-space: nowrap;
  }
  .appointment__head .brand-name { left: 170px; top: 48px; font-size: 30px; }
  .appointment__tab {
    position: absolute; left: 150px; top: 140px; width: 300px; height: 38px;
    background: var(--red);
    clip-path: polygon(0 0, 100% 0, 92% 100%, 8% 100%);
    color: var(--white);
    font-family: "Montserrat", Arial, sans-serif;
    font-weight: 700; font-size: 17px; letter-spacing: 1px;
    display: flex; align-items: center; justify-content: center;
  }
  .write-line {
    position: absolute; left: 90px; right: 60px; height: 0;
    border-top: 1.5px dashed var(--dash);
  }
  .write-line--one { top: 212px; }
  .write-line--two { top: 250px; }
  .day-row, .time-row {
    position: absolute; left: 90px; right: 50px;
    display: flex; align-items: center;
    font-size: 16px; color: var(--ink); letter-spacing: 0.5px;
  }
  .day-row { top: 272px; gap: 30px; }
  .time-row { top: 312px; gap: 12px; }
  .check { display: flex; align-items: center; gap: 8px; }
  .check__box { width: 16px; height: 16px; border: 2px solid var(--red); }
  .blank { width: 150px; border-bottom: 1.5px solid var(--ink); height: 14px; }
  .time-row .spacer { width: 18px; }

  /* ---------- Contact side ---------- */
  .card--contact {
    left: 500px; top: 434px;
    background: linear-gradient(120deg, var(--charcoal-deep) 0%, var(--charcoal) 55%, #303031 100%);
  }
  .card--contact .brand-name { left: 50px; top: 58px; font-size: 38px; }
  .person { position: absolute; left: 50px; top: 186px; }
  .person__name {
    font-family: "Montserrat", Arial, sans-serif; font-weight: 700;
    font-size: 27px; color: var(--red); letter-spacing: 0.5px;
  }
  .person__role { font-size: 19px; color: var(--white); margin-top: 2px; }
  .rule {
    position: absolute; left: 50px; right: 40px; top: 262px;
    border-top: 1.5px solid var(--silver);
  }
  .contact {
    position: absolute; left: 50px; right: 30px;
    font-size: 16px; color: var(--white);
  }
  .contact__address { top: 276px; }
  .contact__lines {
    top: 306px; display: flex; gap: 18px; align-items: center;
  }
  .contact__item { display: flex; align-items: center; gap: 6px; white-space: nowrap; }
  .contact__item svg { width: 15px; height: 15px; fill: var(--red); flex: none; }
</style>
</head>
<body>

  <section class="card card--appointment" aria-label="Appointment side">
    <div class="appointment__head">
      <span class="brand-name">Bellmoor Cardiology</span>
    </div>
    <div class="appointment__tab">APPOINTMENT</div>
    <div class="write-line write-line--one"></div>
    <div class="write-line write-line--two"></div>
    <div class="day-row">
      <span class="check"><span class="check__box"></span>MON</span>
      <span class="check"><span class="check__box"></span>TUE</span>
      <span class="check"><span class="check__box"></span>WED</span>
      <span class="check"><span class="check__box"></span>THU</span>
      <span class="check"><span class="check__box"></span>FRI</span>
      <span class="check"><span class="check__box"></span>SAT</span>
    </div>
    <div class="time-row">
      <span>DATE</span><span class="blank"></span>
      <span class="spacer"></span>
      <span>TIME</span><span class="blank"></span>
      <span class="check"><span class="check__box"></span>AM</span>
      <span class="check"><span class="check__box"></span>PM</span>
    </div>
  </section>

  <section class="card card--contact" aria-label="Contact side">
    <span class="brand-name">Bellmoor Cardiology</span>
    <div class="person">
      <div class="person__name">DANIEL HARTWELL</div>
      <div class="person__role">Manager</div>
    </div>
    <div class="rule"></div>
    <div class="contact contact__address">Your Address, City, State, Zip 0000</div>
    <div class="contact contact__lines">
      <span class="contact__item">
        <svg viewBox="0 0 24 24" aria-hidden="true"><path d="M6.6 10.8a15.1 15.1 0 0 0 6.6 6.6l2.2-2.2c.3-.3.7-.4 1-.2 1.1.4 2.3.6 3.6.6.6 0 1 .4 1 1V20c0 .6-.4 1-1 1A17 17 0 0 1 3 4c0-.6.4-1 1-1h3.5c.6 0 1 .4 1 1 0 1.3.2 2.5.6 3.6.1.3 0 .7-.2 1z"/></svg>
        555-014-2100
      </span>
      <span class="contact__item">
        <svg viewBox="0 0 24 24" aria-hidden="true"><path d="M3 5h18v14H3z M3 5l9 7 9-7" fill="none" stroke="#e3151a" stroke-width="2.4"/></svg>
        hello@bellmoorcardio.com
      </span>
      <span class="contact__item">
        <svg viewBox="0 0 24 24" aria-hidden="true"><circle cx="12" cy="12" r="9.5"/></svg>
        www.bellmoorcardio.com
      </span>
    </div>
  </section>

</body>
</html>
```